Company providing Business Management Services needs modern business card

The business provides services like tender preparation, bank submissions, business health checks, financial and admin support. We want to portray 'Trust', 'Strength' and 'Support'.
2 styles of logo in various formats have been uploaded.
Looking for easy to understand, yet sophisticated and stand out from the crowd.

Target Market(s)

Small and Medium sized businesses

Industry/Entity Type

Business

Contact Information for Business Card

Name - Daniel Vesterby, Description - Manager, Phone - 0472 915 603, Email - danielvesterby@kpwholdingsgroup.example, Work description - Business Management Services.

Requirements
Must have
• Logo

```html
<!DOCTYPE html>
<html lang="en">
<head>
<meta charset="utf-8">
<title>KPW Holdings Group – Business Card</title>
<link rel="stylesheet" href="https://fonts.googleapis.com/css2?family=Lato:wght@400;700&display=swap">
<style>
:root{
  --bg:#e9e6e1;
  --card-white:#fbfbfb;
  --ink:#1e1e1e;
  --ink-soft:#2b2b2b;
  --grey:#6d6d6d;
  --purple:#a24fc0;
  --blue:#3e8fd0;
  --green:#7cc142;
  --yellow:#f2b21b;
  --orange:#f29a1e;
  --text-light:#f1f1f1;
}
*{box-sizing:border-box;margin:0;padding:0}
html,body{width:1200px;height:1023px;overflow:hidden}
body{background:var(--bg);font-family:"Lato",Arial,sans-serif;position:relative}
.card{position:absolute;left:190px;width:820px;height:468px;border-radius:6px;overflow:hidden;box-shadow:0 6px 18px rgba(0,0,0,.18)}
.card--front{top:24px;background:var(--card-white)}
.card--back{top:531px;background:linear-gradient(160deg,var(--ink-soft),var(--ink))}

.pattern-area{position:absolute;left:525px;top:104px;width:265px;height:336px;border-radius:4px;
  background:linear-gradient(135deg,#d9d9d9 0%,#b9b9b9 40%,#cfcfcf 70%,#bdbdbd 100%)}
.holder{position:absolute;right:30px;top:24px;text-align:right}
.holder__name{font-size:30px;font-weight:700;color:var(--purple)}
.holder__title{font-size:18px;color:var(--grey);margin-top:2px}

.brand{position:absolute;left:42px;top:100px;display:flex;align-items:center;gap:14px}
.brand__square{width:44px;height:44px;background:var(--grey);flex:none}
.brand__name{font-size:32px;font-weight:700;color:var(--grey);letter-spacing:.3px;line-height:1.05;white-space:nowrap}

.swoosh{position:absolute;left:0;top:0}
.info{position:absolute;color:var(--text-light)}
.card--front .info{left:170px;top:252px}
.card--back .info{left:60px;top:110px}
.info__heading{font-size:19px;font-weight:700;color:var(--orange);margin-bottom:6px;white-space:nowrap}
.services{list-style:none;margin-bottom:10px}
.services li{font-size:16px;line-height:21px;display:flex;align-items:center;gap:12px;white-space:nowrap}
.services li::before{content:"";width:8px;height:8px;border:2px solid var(--blue);transform:rotate(45deg);flex:none}
.contacts{list-style:none}
.contacts li{font-size:15px;line-height:21px;display:flex;align-items:center;gap:10px;white-space:nowrap}
.contacts svg{flex:none}
.card--back .info__heading{font-size:24px;margin-bottom:8px}
.card--back .services{margin-bottom:16px}
.card--back .services li{font-size:20px;line-height:30px}
.card--back .contacts li{font-size:19px;line-height:30px;gap:12px}
</style>
</head>
<body>

<section class="card card--front">
  <div class="pattern-area" role="img" aria-label="Brand stripe pattern"></div>
  <div class="holder">
    <p class="holder__name">Daniel Vesterby</p>
    <p class="holder__title">Manager</p>
  </div>
  <div class="brand">
    <span class="brand__square"></span>
    <span class="brand__name">KPW Holdings Group</span>
  </div>
  <svg class="swoosh" width="820" height="468" viewBox="0 0 820 468" aria-hidden="true">
    <defs>
      <linearGradient id="spectrum" x1="0" y1="0" x2="1" y2="0">
        <stop offset="0" stop-color="var(--purple)"/>
        <stop offset=".45" stop-color="var(--blue)"/>
        <stop offset=".75" stop-color="var(--green)"/>
        <stop offset="1" stop-color="var(--yellow)"/>
      </linearGradient>
      <linearGradient id="panel" x1="0" y1="0" x2="1" y2="1">
        <stop offset="0" stop-color="#333"/>
        <stop offset="1" stop-color="#161616"/>
      </linearGradient>
    </defs>
    <path d="M0 290 C150 240 330 175 505 150 L505 468 L0 468 Z" fill="url(#spectrum)"/>
    <path d="M0 302 C155 252 335 187 505 162 L505 468 L0 468 Z" fill="url(#panel)"/>
  </svg>
  <div class="info">
    <p class="info__heading">Business Management Services</p>
    <ul class="services">
      <li>Tender Preparation</li>
      <li>Bank Submissions</li>
      <li>Business Health Checks</li>
      <li>Financial and Admin Support</li>
    </ul>
    <ul class="contacts">
      <li><svg width="16" height="16" viewBox="0 0 16 16"><rect width="16" height="16" rx="3" fill="var(--green)"/><path d="M4 4h3l1 3-2 1a6 6 0 0 0 2 2l1-2 3 1v3c-5 0-8-3-8-8z" fill="#1e1e1e"/></svg>0472 915 603</li>
      <li><svg width="16" height="16" viewBox="0 0 16 16"><rect width="16" height="16" rx="3" fill="var(--green)"/><path d="M3 5h10v7H3z M3 5l5 4 5-4" fill="none" stroke="#1e1e1e" stroke-width="1.4"/></svg>danielvesterby@kpwholdingsgroup.example</li>
      <li><svg width="16" height="16" viewBox="0 0 16 16"><circle cx="8" cy="8" r="8" fill="var(--green)"/><path d="M2 8h12M8 2c-3 3-3 9 0 12M8 2c3 3 3 9 0 12" fill="none" stroke="#1e1e1e" stroke-width="1.2"/></svg>www.kpwholdingsgroup.example</li>
    </ul>
  </div>
</section>

<section class="card card--back">
  <div class="info">
    <p class="info__heading">Business Management Services</p>
    <ul class="services">
      <li>Tender Preparation</li>
      <li>Bank Submissions</li>
      <li>Business Health Checks</li>
      <li>Financial and Admin Support</li>
    </ul>
    <ul class="contacts">
      <li><svg width="18" height="18" viewBox="0 0 16 16"><rect width="16" height="16" rx="3" fill="var(--green)"/><path d="M4 4h3l1 3-2 1a6 6 0 0 0 2 2l1-2 3 1v3c-5 0-8-3-8-8z" fill="#1e1e1e"/></svg>0472 915 603</li>
      <li><svg width="18" height="18" viewBox="0 0 16 16"><rect width="16" height="16" rx="3" fill="var(--green)"/><path d="M3 5h10v7H3z M3 5l5 4 5-4" fill="none" stroke="#1e1e1e" stroke-width="1.4"/></svg>danielvesterby@kpwholdingsgroup.example</li>
      <li><svg width="18" height="18" viewBox="0 0 16 16"><circle cx="8" cy="8" r="8" fill="var(--green)"/><path d="M2 8h12M8 2c-3 3-3 9 0 12M8 2c3 3 3 9 0 12" fill="none" stroke="#1e1e1e" stroke-width="1.2"/></svg>www.kpwholdingsgroup.example</li>
    </ul>
  </div>
</section>

</body>
</html>
```